"Bright Hollow Craft Dwellings" need a busines Card Design got Builder

We need a business card design for a company based in Milford, Michigancalled Bright Hollow Craft Dwellings - has been recognized as a premier custom home builder. Distinguished by outstanding craftmanship and timeless beauty. Our custom home can be found in the most prestigious communities in Michigan. The homes are built with ICF (insulated concrete homes) which is green, allergy free, fire free, mold free and quitter. Our slogan "building one dream at a Time" and also we are ICF distributor for the state of Michigan

Target Market(s)

Anyone who is making over $100,000 a year and who wants to have totally custom built home. Ages from 29 up to 60 years old

Industry/Entity Type

Concrete

Contact Information for Business Card

we want to use - green, black, gray or blue colors - we want to look different with our business cards, because we built homes only with ICF, green, healthier and highly energy efficient homes.

Requirements
Must have
• I have logo that I attached and we have been using the logo (the only green home)
Nice to have
• should look quality business card,

```html
<!DOCTYPE html>
<html lang="en">
<head>
<meta charset="utf-8">
<title>Bright Hollow Craft Dwellings — Business Card</title>
<link rel="stylesheet" href="https://fonts.googleapis.com/css2?family=Lato:wght@300;400;700&display=swap">
<style>
  :root {
    --page-bg: #e9e7e3;
    --card-bg: #ffffff;
    --band-dark: #3f3a78;
    --band-light: #9c98c2;
    --tab: #7a75a8;
    --brand-gray: #9a9aa3;
    --text-gray: #9a9aa0;
    --icon-blue: #3b5fa8;
    --faint: #eceef3;
    --badge: #8a8a8f;
  }
  * { box-sizing: border-box; margin: 0; padding: 0; }
  html, body {
    width: 1200px; height: 900px; overflow: hidden;
    background: var(--page-bg);
    font-family: "Lato", sans-serif;
  }
  .business-card {
    position: absolute; left: 100px; top: 164px;
    width: 1000px; height: 572px;
    background: var(--card-bg);
    box-shadow: 0 10px 30px rgba(0,0,0,.18);
    overflow: hidden;
  }
  .backdrop-circle {
    position: absolute; right: 90px; top: 30px;
    width: 430px; height: 430px; border-radius: 50%;
    background: var(--faint);
  }
  .brand {
    position: absolute; left: 74px; top: 120px;
    display: flex; align-items: center; gap: 22px;
  }
  .brand-dot {
    width: 104px; height: 104px; border-radius: 50%;
    background: var(--band-dark);
  }
  .brand-name {
    font-weight: 300; color: var(--brand-gray);
    font-size: 30px; line-height: 0.95; letter-spacing: 1px;
    text-transform: uppercase;
  }
  .ribbon {
    position: absolute; left: 0; right: 0; top: 258px; height: 54px;
    background: linear-gradient(90deg, var(--band-light) 0%, var(--tab) 45%, var(--band-dark) 100%);
    display: flex; align-items: center; justify-content: space-between;
    padding: 0 28px 0 56px;
    color: #fff;
  }
  .person { font-size: 29px; font-weight: 400; }
  .person .divider { margin: 0 6px; }
  .person .role { font-size: 20px; text-transform: uppercase; letter-spacing: .5px; }
  .slogan { font-size: 19px; font-weight: 700; text-transform: uppercase; letter-spacing: .5px; }
  .contact-list {
    position: absolute; left: 74px; top: 366px;
    list-style: none;
  }
  .contact-list li {
    display: flex; align-items: center; gap: 18px;
    font-size: 24px; color: var(--text-gray); line-height: 38px;
  }
  .contact-list svg { width: 20px; height: 20px; fill: var(--icon-blue); }
  .partner-badge {
    position: absolute; right: 48px; bottom: 52px;
    width: 72px; height: 56px;
    background: var(--badge); border: 3px solid #d0d0d4;
  }
</style>
</head>
<body>
  <div class="business-card">
    <div class="backdrop-circle"></div>

    <div class="brand">
      <div class="brand-dot"></div>
      <div class="brand-name">Bright Hollow<br>Craft Dwellings</div>
    </div>

    <div class="ribbon">
      <span class="person">Mark Ellison<span class="divider">|</span><span class="role">Director</span></span>
      <span class="slogan">Building one dream at a time</span>
    </div>

    <ul class="contact-list">
      <li>
        <svg viewBox="0 0 24 24" aria-hidden="true"><path d="M6.6 10.8a15 15 0 006.6 6.6l2.2-2.2c.3-.3.7-.4 1-.2 1.1.4 2.3.6 3.6.6.6 0 1 .4 1 1V20c0 .6-.4 1-1 1A17 17 0 013 4c0-.6.4-1 1-1h3.5c.6 0 1 .4 1 1 0 1.3.2 2.5.6 3.6.1.3 0 .7-.2 1z"/></svg>
        450 41 262
      </li>
      <li>
        <svg viewBox="0 0 24 24" aria-hidden="true"><path d="M7 3h10v5H7zM4 9h16a2 2 0 012 2v6h-4v4H6v-4H2v-6a2 2 0 012-2zm4 6v4h8v-4z"/></svg>
        450 41 288
      </li>
      <li>
        <svg viewBox="0 0 24 24" aria-hidden="true"><path d="M2 5h20v14H2zm2 2v.5l8 5 8-5V7zm0 2.8V17h16V9.8l-8 5z"/></svg>
        mellison@brighthollow.com
      </li>
      <li>
        <svg viewBox="0 0 24 24" aria-hidden="true"><path d="M12 2a10 10 0 100 20 10 10 0 000-20zm6.9 9h-3a15 15 0 00-1.3-5.9A8 8 0 0118.9 11zM12 4c.9 1.3 1.7 3.8 1.9 7h-3.8C10.3 7.8 11.1 5.3 12 4zM9.4 5.1A15 15 0 008.1 11h-3a8 8 0 014.3-5.9zM5.1 13h3a15 15 0 001.3 5.9A8 8 0 015.1 13zm6.9 7c-.9-1.3-1.7-3.8-1.9-7h3.8c-.2 3.2-1 5.7-1.9 7zm2.6-1.1a15 15 0 001.3-5.9h3a8 8 0 01-4.3 5.9z"/></svg>
        www.brighthollow.com
      </li>
    </ul>

    <div class="partner-badge" aria-hidden="true"></div>
  </div>
</body>
</html>
```